Pelkman Agency (http://pa.quorvexstudio.com/)

We are looking for a similar design to what we have, but more professional looking and cleaned up with links and logo that is not so grainy looking. We are an independent insurance agency marketing to personal and commercial clients. We offer all commercial lines markets and all personal lines. We target excavators, landscapers, restaurants, golf courses, contractors. Please look at http://pa.quorvexstudio.com/ which we had designed but do not like it, it will give you an idea of what we are looking for.

Target Market(s)

Commercial and personal insurance. All business products and all personal (homeowners, auto, antique auto, umbrella)

Industry/Entity Type

It Professional

Logo Text

Knowledge Building Your Assurance

Number of Pages Required

5+ page

Colors
000000
848484
0255a3

```html
<!DOCTYPE html>
<html lang="en">
<head>
<meta charset="utf-8">
<title>Pelkman Agency</title>
<link href="https://fonts.googleapis.com/css2?family=Open+Sans:wght@300;400;600;700;800&display=swap" rel="stylesheet">
<style>
:root{
  --blue:#0255a3;
  --blue-deep:#054b9c;
  --blue-light:#5d8fe0;
  --ink:#000000;
  --text:#333333;
  --grey:#848484;
  --soft:#f3f3f5;
  --footer:#2b2b2b;
  --footer-deep:#1f1f1f;
  --field:#1a1a1a;
  --white:#ffffff;
}
*{box-sizing:border-box;margin:0;padding:0}
html,body{width:1200px;height:3358px;overflow:hidden}
body{font-family:"Open Sans",Arial,sans-serif;color:var(--text);background:var(--white);position:relative}
.section{position:relative;width:1200px;overflow:hidden}
.abs{position:absolute}

/* header */
.site-header{height:112px;background:var(--soft);border-top:5px solid var(--blue)}
.brand{left:98px;top:22px;display:flex;align-items:center;gap:12px}
.brand-mark{width:52px;height:52px;border-radius:50%;background:var(--blue)}
.brand-name{font-size:34px;font-weight:700;color:var(--blue);line-height:1;letter-spacing:1px}
.brand-sub{font-size:16px;font-weight:400;color:var(--blue);letter-spacing:5px;margin-top:4px;padding-left:40px}
.call{left:924px;top:12px;display:flex;gap:10px;align-items:center}
.call-title{font-size:20px;font-weight:600;color:var(--blue);line-height:1.1}
.call-phone{font-size:16px;color:var(--grey)}

/* nav */
.main-nav{height:58px;background:var(--blue)}
.nav-list{left:105px;top:0;display:flex;list-style:none;height:58px}
.nav-list li{height:58px;line-height:58px;padding:0 16px;color:var(--white);font-size:11px;font-weight:700;text-transform:uppercase}
.nav-list li.active{background:var(--blue-light)}
.search{left:870px;top:12px;width:232px;height:34px;background:var(--white);border:1px solid #c9d6ea}
.search svg{position:absolute;right:10px;top:6px}

/* hero */
.hero{height:515px;background:linear-gradient(160deg,#6a6d70 0%,#3b3e42 45%,#1f2023 100%)}
.hero-photo{inset:0;background:radial-gradient(ellipse at 62% 58%,#2f5fa8 0%,#28446e 22%,transparent 50%)}
.hero-title{left:130px;top:336px;font-size:68px;font-weight:400;color:var(--white);letter-spacing:1px}
.hero-arrow{top:236px}

/* welcome */
.welcome{height:340px;background:var(--soft);text-align:center}
.welcome h1{position:absolute;left:0;right:0;top:68px;font-size:50px;font-weight:800;color:var(--text);letter-spacing:1px}
.welcome p{position:absolute;left:110px;right:110px;top:143px;font-size:12.5px;line-height:1.45;color:#444}
.btn{display:inline-block;background:var(--blue);color:var(--white);font-size:13px;text-align:center}
.welcome .btn{position:absolute;left:546px;top:244px;width:110px;height:40px;line-height:40px}

/* services */
.services{height:471px;background:var(--blue-deep);text-align:center;color:var(--white)}
.services h2{position:absolute;left:0;right:0;top:48px;font-size:34px;font-weight:800}
.services .lead{position:absolute;left:0;right:0;top:97px;font-size:13px}
.hex{top:162px;width:242px;height:213px;clip-path:polygon(25% 0,75% 0,100% 50%,75% 100%,25% 100%,0 50%);background:var(--white)}
.hex-inner{position:absolute;inset:4px;clip-path:polygon(25% 0,75% 0,100% 50%,75% 100%,25% 100%,0 50%);background:linear-gradient(160deg,#c8c2b8,#8b8377 60%,#5a5048)}
.hex-band{position:absolute;left:0;right:0;top:104px;height:82px;background:rgba(5,75,156,.88)}
.hex-label{position:absolute;left:0;right:0;top:112px;font-size:14px}
.hex-btn{position:absolute;left:71px;top:140px;width:92px;height:24px;line-height:22px;border:1px solid var(--white);font-size:9px}

/* service center & news */
.info{height:501px;background:var(--soft)}
.section-title{font-size:34px;font-weight:300;line-height:1.05;text-transform:uppercase}
.sc-title{left:98px;top:48px;color:#555}
.sc-sub{left:98px;top:150px;width:470px;font-size:15.5px;color:var(--grey);text-transform:uppercase;line-height:1.3}
.sc-text{left:98px;top:205px;width:480px;font-size:11px;color:#b0b0b0;line-height:1.55}
.sc-list{top:320px;list-style:none;font-size:12px;color:#555;text-transform:uppercase}
.sc-list li{height:35px;padding-left:26px;position:relative}
.sc-list li::before{content:"";position:absolute;left:0;top:3px;width:6px;height:6px;border-right:2px solid var(--blue);border-top:2px solid var(--blue);transform:rotate(45deg)}
.news-title{left:616px;top:48px;color:var(--blue)}
.news-card{top:160px;width:234px}
.news-img{height:134px;background:linear-gradient(150deg,#e9eaec,#b9bdc4 60%,#8d8f93)}
.news-date{position:absolute;left:0;top:85px;width:52px;height:49px;background:var(--blue-light);color:var(--white);text-align:center}
.news-date b{display:block;font-size:28px;font-weight:300;line-height:34px}
.news-date span{display:block;font-size:10px;line-height:12px}
.news-head{margin-top:34px;font-size:15px;color:#444;text-transform:uppercase}
.news-meta{font-size:11px;color:var(--blue);text-transform:uppercase}
.news-text{margin-top:8px;font-size:10.5px;color:#b0b0b0;line-height:1.5}

/* testimonials */
.testimonials{height:488px;background:linear-gradient(180deg,#3a3633,#262321 55%,#1c1a18);text-align:center;color:var(--white)}
.testimonials h2{position:absolute;left:0;right:0;top:40px;font-size:44px;font-weight:400}
.quote{left:553px;top:118px}
.testimonials h3{position:absolute;left:0;right:0;top:216px;font-size:24px;font-weight:400;letter-spacing:.5px}
.testimonials p{position:absolute;left:100px;right:100px;top:257px;font-size:13px;font-weight:600;line-height:1.4}
.outline-btn{position:absolute;left:545px;top:366px;width:108px;height:40px;line-height:38px;border:2px solid var(--white);font-size:13px}

/* video */
.video{height:426px;background:var(--blue-deep);color:var(--white)}
.player{left:100px;top:72px;width:510px;height:290px;background:linear-gradient(135deg,#d9d7d4,#a9a6a1 50%,#56524e)}
.player-bar{position:absolute;left:0;right:0;bottom:0;height:32px;background:rgba(0,0,0,.85)}
.progress{position:absolute;left:42px;right:60px;top:14px;height:4px;background:#666}
.progress i{display:block;width:45%;height:4px;background:#c0212e}
.video-title{left:675px;top:62px;font-size:30px}
.video-sub{left:679px;top:102px;font-size:13px;color:#a9c4ef}
.clip{left:679px;display:flex;gap:18px;width:420px}
.clip-thumb{position:relative;width:86px;height:70px;background:linear-gradient(135deg,#f1f1f1,#9aa0a8);border:3px solid var(--white)}
.clip-num{position:absolute;right:-14px;top:22px;width:26px;height:26px;border-radius:50%;background:#1d2a4a;border:2px solid var(--white);font-size:12px;text-align:center;line-height:22px}
.clip h4{font-size:15px;font-weight:400;line-height:1.2;margin-top:2px}
.clip p{font-size:11px;color:#c7d6ef}
.clip a{font-size:11px;color:#8fb2ec}

/* footer */
.site-footer{height:385px;background:var(--footer);color:#d0d0d0}
.foot-col{top:38px}
.foot-col h5{font-size:24px;font-weight:400;color:var(--white);margin-bottom:26px}
.contact-lines{font-size:11px;line-height:2.1}
.links{list-style:none;font-size:11px}
.links li{height:34px;line-height:34px;color:#6f9bea;border-bottom:1px solid #3a3a3a;padding-left:12px;position:relative}
.links li::before{content:"›";position:absolute;left:0;color:#6f9bea}
.tweet{font-size:11px;line-height:1.6;margin-bottom:14px;width:225px}
.tweet b{color:#6f9bea;font-weight:400}
.field{width:228px;height:36px;background:var(--field);margin-bottom:8px;font-size:11px;color:#888;padding:10px 14px}
.field.tall{height:82px}
.submit{display:block;width:74px;height:36px;line-height:36px;text-align:center;background:var(--blue-light);color:var(--white);font-size:11px;margin-top:14px}
.copyright{height:62px;background:var(--footer-deep);border-top:1px solid #3c3c3c}
.copyright p{position:absolute;left:98px;top:22px;font-size:12px;color:var(--grey)}
</style>
</head>
<body>

<header class="section site-header">
  <div class="abs brand">
    <div class="brand-mark"></div>
    <div>
      <div class="brand-name">PELKMAN</div>
      <div class="brand-sub">AGENCY</div>
    </div>
  </div>
  <div class="abs call">
    <svg width="42" height="42" viewBox="0 0 42 42"><circle cx="21" cy="21" r="20" fill="#e3e3e3"/><path d="M10 22a11 11 0 0 1 22 0" fill="none" stroke="#333" stroke-width="3"/><rect x="8" y="20" width="6" height="10" rx="2" fill="#333"/><rect x="28" y="20" width="6" height="10" rx="2" fill="#333"/><circle cx="21" cy="22" r="7" fill="#c0212e"/></svg>
    <div>
      <div class="call-title">Call Us</div>
      <div class="call-phone">+123 555 0148</div>
    </div>
  </div>
</header>

<nav class="section main-nav">
  <ul class="abs nav-list">
    <li class="active">Home</li>
    <li>About Us</li>
    <li>Personal Insurance</li>
    <li>Business Insurance</li>
    <li>Service Center</li>
    <li>Contact Us</li>
  </ul>
  <div class="abs search">
    <svg width="22" height="22" viewBox="0 0 22 22"><circle cx="9" cy="9" r="7" fill="none" stroke="#0255a3" stroke-width="2.5"/><path d="M14 14l6 6" stroke="#0255a3" stroke-width="3"/></svg>
  </div>
</nav>

<section class="section hero">
  <div class="abs hero-photo" role="img" aria-label="Blue hatchback car parked in a large industrial hall"></div>
  <h2 class="abs hero-title">Auto Insurance</h2>
  <svg class="abs hero-arrow" style="left:8px" width="22" height="40" viewBox="0 0 22 40"><path d="M18 4L4 20l14 16" fill="none" stroke="#fff" stroke-width="4"/></svg>
  <svg class="abs hero-arrow" style="right:8px" width="22" height="40" viewBox="0 0 22 40"><path d="M4 4l14 16L4 36" fill="none" stroke="#fff" stroke-width="4"/></svg>
</section>

<section class="section welcome">
  <h1>WELCOME TO OUR WEBSITE</h1>
  <p>At vero eos et accusamus et iusto odio dignissimos ducimus qui blanditiis praesentium voluptatum deleniti atque corrupti quos dolores et quasmolestias excepturi sint occaecati cupiditate non provident, similique sunt in culpa qui officia deserunt mollitia animi, id est laborum et dolorum fuga. Et harum quidem rerum facilis est et expedita distinctio. Nam libero tempore, cum soluta nobis est eligendi optio cumque nihil impedit quo minus id quod maxime placeat facere possimu</p>
  <span class="btn">Read More</span>
</section>

<section class="section services">
  <h2>OUR SERVICES</h2>
  <p class="lead">At vero eos et accusamus et iusto odio dignissimos ducimus qui blanditiis praesentium voluptatum deleniti</p>
  <div class="abs hex" style="left:96px"><div class="hex-inner" role="img" aria-label="Business people in a meeting"></div><div class="hex-band"></div><div class="hex-label">Business Insurance</div><div class="hex-btn">Get a Quote</div></div>
  <div class="abs hex" style="left:349px"><div class="hex-inner" role="img" aria-label="Driver seated in a car"></div><div class="hex-band"></div><div class="hex-label">Auto Insurance</div><div class="hex-btn">Get a Quote</div></div>
  <div class="abs hex" style="left:602px"><div class="hex-inner" role="img" aria-label="Family playing together outdoors"></div><div class="hex-band"></div><div class="hex-label">Life Insurance</div><div class="hex-btn">Get a Quote</div></div>
  <div class="abs hex" style="left:855px"><div class="hex-inner" role="img" aria-label="Model of a family house"></div><div class="hex-band"></div><div class="hex-label">Home Insurance</div><div class="hex-btn">Get a Quote</div></div>
</section>

<section class="section info">
  <h2 class="abs section-title sc-title">Service<br>Center</h2>
  <p class="abs sc-sub">Mes cuml dia sed ineniasinge dolor ipsum commete ipsum comnetus mes ineniasinge dolor.</p>
  <p class="abs sc-text">Dolor nunc vule pulvinar ips dol consec. Donec temp ertet lacinia ultricie sapien duce commete duis lectus ligula tincidunt bus nullam dolor nec. sed quam accumsan dolore. Condime netus tellum ullamco adipiscing ipsum molestie euismod estibulum vel libero ipsum sit amet sollicitudin ante. Aenean imperdiet aliquet tincidunt.</p>
  <ul class="abs sc-list" style="left:98px">
    <li>Lorem ipsum dolor sit.</li>
    <li>Consectetur adipiscing.</li>
    <li>In euismod est quis arc.</li>
    <li>Venenatis imperdiet etia.</li>
  </ul>
  <ul class="abs sc-list" style="left:356px">
    <li>Lorem ipsum dolor sit.</li>
    <li>Consectetur adipiscing.</li>
    <li>In euismod est quis arc.</li>
    <li>Venenatis imperdiet etia.</li>
  </ul>

  <h2 class="abs section-title news-title">Featured<br>News</h2>
  <article class="abs news-card" style="left:616px">
    <div class="news-img" role="img" aria-label="Colleagues working at an office desk"></div>
    <div class="news-date"><b>27</b><span>MAY</span></div>
    <h3 class="news-head">Donec facilisi ulet</h3>
    <div class="news-meta">Lorem ipsum dolore</div>
    <p class="news-text">Aliquam dapibus tincidunt metus. Praesent justo dolor, lobortis quis, lobortis dignissim, pulvinar ac, lorem. Lorem ipsum dolor sit amet, consectetuer.</p>
  </article>
  <article class="abs news-card" style="left:868px">
    <div class="news-img" role="img" aria-label="Group of smiling team members"></div>
    <div class="news-date"><b>14</b><span>MAR</span></div>
    <h3 class="news-head">Donec facilisi ulet</h3>
    <div class="news-meta">Lorem ipsum dolore</div>
    <p class="news-text">Aliquam dapibus tincidunt metus. Praesent justo dolor, lobortis quis, lobortis dignissim, pulvinar ac, lorem. Lorem ipsum dolor sit amet, consectetuer.</p>
  </article>
</section>

<section class="section testimonials" role="img" aria-label="Dark close-up of a computer keyboard behind the testimonial">
  <h2>TESTIMONIALS</h2>
  <svg class="abs quote" width="94" height="70" viewBox="0 0 94 70"><path d="M4 66V40C4 18 14 6 34 2v12C24 18 20 26 20 34h16v32zM54 66V40c0-22 10-34 30-38v12c-10 4-14 12-14 20h16v32z" fill="#fff"/></svg>
  <h3>EU FUGIAT NULLA PARIATUR</h3>
  <p>Lorem ipsum dolor sit amet conse ctetur adipisicing elit, sed do eiusmod tempor incididunt ut labore et dolore magna aliqua. Ut enim ad minim veniam, quis nostrud exercitation ullamco laboris nisi ut aliquip ex ea commodo consequat. Duis aute irure dolor in reprehenderit in voluptate velit esse cillum dolore eu fugiat nulla pariatur. Excepteur sint occaecat cupidatat non proident,.</p>
  <span class="outline-btn">SEE ALL</span>
</section>

<section class="section video">
  <div class="abs player" role="img" aria-label="Video still of a bright office with large white title lettering">
    <div class="player-bar">
      <svg style="position:absolute;left:14px;top:9px" width="14" height="14" viewBox="0 0 14 14"><path d="M2 1l11 6-11 6z" fill="#fff"/></svg>
      <div class="progress"><i></i></div>
      <svg style="position:absolute;right:14px;top:8px" width="16" height="16" viewBox="0 0 16 16"><path d="M1 5V1h4M11 1h4v4M15 11v4h-4M5 15H1v-4" fill="none" stroke="#fff" stroke-width="2"/></svg>
    </div>
  </div>
  <h2 class="abs video-title">Featured Video</h2>
  <p class="abs video-sub">Mollis Ipsum Tortor Vulputate</p>
  <div class="abs clip" style="top:132px">
    <div class="clip-thumb" role="img" aria-label="Website screenshot thumbnail"><span class="clip-num">1</span></div>
    <div><h4>Lorem ipsum dolor sit amet, consectetur</h4><p>adipiscing elitgger gravida velit quis dolo</p><a>Read More</a></div>
  </div>
  <div class="abs clip" style="top:212px">
    <div class="clip-thumb" role="img" aria-label="Mobile phones thumbnail"><span class="clip-num">2</span></div>
    <div><h4>Lorem ipsum dolor sit amet, consectetur</h4><p>adipiscing elitgger gravida velit quis dolo</p><a>Read More</a></div>
  </div>
  <div class="abs clip" style="top:292px">
    <div class="clip-thumb" role="img" aria-label="Hand holding a device thumbnail"><span class="clip-num">3</span></div>
    <div><h4>Lorem ipsum dolor sit amet, consectetur</h4><p>adipiscing elitgger gravida velit quis dolo</p><a>Read More</a></div>
  </div>
</section>

<footer class="section site-footer">
  <div class="abs foot-col" style="left:98px">
    <h5>Contact</h5>
    <div class="contact-lines">(Melbourne Office / Head Office)<br>Level 4, Suite 402 / 18 Harrow Lane,<br>Eastbrook, VIC 3011<br>Phone: (03) 5550 1742<br>(Brisbane Office)<br>Shop 2/91 Wattle Road,<br>Kelvale, QLD 4120<br>(07) 5550 3318</div>
  </div>
  <div class="abs foot-col" style="left:356px;width:230px">
    <h5>Quick Links</h5>
    <ul class="links">
      <li>Lorem ipsum dolor sit</li>
      <li>Amet consectetur</li>
      <li>Praesent vel sem id</li>
      <li>Curabitur hendrerit est</li>
      <li>Aliquam eget erat nec sapien</li>
      <li>Cras id augue nunc</li>
      <li>Sed a nulla urna</li>
    </ul>
  </div>
  <div class="abs foot-col" style="left:610px">
    <h5>Latest Tweets</h5>
    <p class="tweet"><b>@namehere</b> Justoid nonummy laoreet phasellent penatoque in antequse pellus elis eget tincidunt. Nequatdui laoreet justo a non tellus laoreetut vitae doloreet<br>1 day ago</p>
    <p class="tweet"><b>@namehere</b> Justoid nonummy laoreet phasellent penatoque in antequse pellus elis eget tincidunt. Nequatdui laoreet justo a non tellus laoreetut vitae doloreet<br>1 day ago</p>
  </div>
  <div class="abs foot-col" style="left:872px">
    <h5>Contact Us</h5>
    <div class="field">Full Name</div>
    <div class="field">Email Address</div>
    <div class="field">Subject</div>
    <div class="field tall">Message</div>
    <span class="submit">SUBMIT</span>
  </div>
</footer>

<div class="section copyright">
  <p>Copyright © 2015 Pelkman Agency - All Rights Reserved</p>
</div>

</body>
</html>
```